New Premium Rum

We need label for an exclusive rum named after our family name. Ron Valcastro. This rum sells for 50 US and is aged at least 10 years. There is a lot of tradition involved. This rum is from Belize, Central America.
My website is www.quietcovedistill.com if you want to check some of our other products.

Reason: I would like to get more designs to view and have more time to give feedback.

Reason: I did not get designs I really like

```html
<!DOCTYPE html>
<html lang="en">
<head>
<meta charset="utf-8">
<title>Ron Valcastro Rum Label</title>
<link rel="stylesheet" href="https://fonts.googleapis.com/css2?family=Teko:wght@500;600&family=Saira+Condensed:wght@500&display=swap">
<style>
  :root {
    --backdrop: #ececec;
    --label-cream: #f2e8b4;
    --label-ink: #4a4431;
  }
  html, body {
    margin: 0;
    padding: 0;
    width: 1200px;
    height: 1000px;
    overflow: hidden;
    background: var(--backdrop);
  }
  .canvas {
    position: relative;
    width: 1200px;
    height: 1000px;
  }
  .label {
    position: absolute;
    left: 360px;
    top: 70px;
    width: 480px;
    height: 860px;
    color: var(--label-ink);
    font-family: "Teko", "Arial Narrow", sans-serif;
    text-align: center;
  }
  .label p, .label h1 { margin: 0; position: absolute; left: 0; right: 0; line-height: 1; }
  .label-shape { position: absolute; inset: 0; }
  .label-body { fill: var(--label-cream); }
  .label-frame { fill: none; stroke: var(--label-ink); stroke-width: 8; }
  .barrel-emblem {
    position: absolute;
    left: 212px;
    top: 58px;
    width: 56px;
    height: 56px;
    border-radius: 50%;
    background: radial-gradient(circle, #8d8562 0%, var(--label-ink) 100%);
  }
  .brand-name {
    top: 152px;
    font-weight: 500;
    font-size: 58px;
    letter-spacing: 1px;
  }
  .brand-kind {
    top: 200px;
    font-weight: 600;
    font-size: 86px;
  }
  .ship-medallion {
    position: absolute;
    left: 100px;
    top: 298px;
    width: 280px;
    height: 280px;
    border-radius: 50%;
    border: 3px solid var(--label-ink);
    box-sizing: border-box;
    background: radial-gradient(circle, #6f6748 0%, var(--label-ink) 55%, var(--label-cream) 56%);
  }
  .age-statement {
    top: 596px;
    font-weight: 600;
    font-size: 68px;
  }
  .origin {
    top: 672px;
    font-family: "Saira Condensed", "Arial Narrow", sans-serif;
    font-weight: 500;
    font-size: 14px;
    letter-spacing: 2px;
  }
  .strength {
    top: 750px;
    font-weight: 500;
    font-size: 40px;
  }
</style>
</head>
<body>
<main class="canvas">
  <section class="label">
    <svg class="label-shape" width="480" height="860" viewBox="0 0 480 860" aria-hidden="true">
      <path class="label-body" d="M0,140 Q30,140 30,110 H80 Q110,110 110,80 V30 Q140,30 140,0 H340 Q340,30 370,30 V80 Q370,110 400,110 H450 Q450,140 480,140 V720 Q450,720 450,750 H400 Q370,750 370,780 V830 Q340,830 340,860 H140 Q140,830 110,830 V780 Q110,750 80,750 H30 Q30,720 0,720 Z"/>
      <path class="label-frame" d="M20,150 Q46,150 46,128 H92 Q128,128 128,92 V48 Q158,48 158,20 H322 Q322,48 352,48 V92 Q352,128 388,128 H434 Q434,150 460,150 V710 Q434,710 434,732 H388 Q352,732 352,768 V812 Q322,812 322,840 H158 Q158,812 128,812 V768 Q128,732 92,732 H46 Q46,710 20,710 Z"/>
    </svg>
    <div class="barrel-emblem" role="img" aria-label="Small barrel emblem on a ribbon"></div>
    <h1 class="brand-name">RON VALCASTRO</h1>
    <p class="brand-kind">RUM</p>
    <div class="ship-medallion" role="img" aria-label="Silhouette of a tall sailing ship inside a hand-drawn circle"></div>
    <p class="age-statement">10 YEARS OLD</p>
    <p class="origin">PRODUCED IN BELIZE, CENTRAL AMERICA</p>
    <p class="strength">40%</p>
  </section>
</main>
</body>
</html>
```